Business card for Sports Apparel business

DOUBLE SIDED DESIGN
We need business cards for a new sports apparel business. We are developing a protective headband for soccer initially.
Quorvane is focused on designing and developing head protection products to reduce the likelihood of concussion when playing sports. Exploring and understanding medical insights, material science research, current and former players experiences and governing bodies guidelines has allowed Quorvane to develop the safety, style, form and function requirements of a suitable product to bring to market.
Target Market(s)
Mums buying kits for the sons and daughters. Amateur footballers.
Industry/Entity Type
Sporting Good
Contact Information for Business Card
Martin Ellwood - CEO
Mobile: +44 7700123456
Email: martin@quorvane.co.uk
Tel: 0208 1234567
Rosalind Pyke - COO
Mob: +44 7700 654321
Email: rosalind@quorvane.co.uk
Tel: 0208 1234567
Gordon Haley - CCO
Mob: +44 7700 987654
Email: gordon@quorvane.co.uk
Tel: 0208 1234567
Look and feel
Each slider illustrates characteristics of the customer's brand and the style your logo design should communicate.

```html
<!DOCTYPE html>
<html lang="en">
<head>
<meta charset="UTF-8">
<title>Quorvane Business Card</title>
<link rel="stylesheet" href="https://fonts.googleapis.com/css2?family=Montserrat:wght@400;600;700&display=swap">
<style>
  :root {
    --page-bg: #e6e7e9;
    --card-black: #111112;
    --card-white: #ffffff;
    --brand-blue: #0a5c97;
    --text-grey: #5a5a5c;
    --brand-grey: #8a8a8c;
    --text-light: #ffffff;
  }
  * { box-sizing: border-box; margin: 0; padding: 0; }
  html, body {
    width: 1200px;
    height: 1015px;
    overflow: hidden;
    background: var(--page-bg);
    font-family: "Montserrat", Arial, sans-serif;
  }
  .sheet {
    position: relative;
    width: 1200px;
    height: 1015px;
  }
  .card {
    position: absolute;
    left: 250px;
    width: 700px;
    height: 400px;
    overflow: hidden;
    box-shadow: 0 10px 30px rgba(0,0,0,0.18);
  }
  .card--front {
    top: 70px;
    background: var(--card-black);
    display: flex;
    align-items: center;
    justify-content: center;
  }
  .brand {
    display: flex;
    align-items: center;
    gap: 16px;
  }
  .brand__square {
    width: 26px;
    height: 26px;
    background: var(--brand-blue);
  }
  .brand__name {
    font-weight: 700;
    font-size: 46px;
    letter-spacing: 3px;
    color: var(--brand-grey);
    text-transform: uppercase;
  }
  .card--back {
    top: 545px;
    background: var(--card-white);
  }
  .name-frame {
    position: absolute;
    left: 228px;
    top: 110px;
    width: 378px;
    height: 108px;
    border: 3px solid var(--brand-blue);
    display: flex;
    flex-direction: column;
    align-items: center;
    justify-content: center;
    color: var(--text-grey);
  }
  .name-frame__name {
    font-weight: 700;
    font-size: 30px;
    letter-spacing: 0.5px;
    text-transform: uppercase;
  }
  .name-frame__role {
    font-weight: 400;
    font-size: 22px;
    margin-top: 2px;
  }
  .contact-band {
    position: absolute;
    left: 0;
    bottom: 0;
    width: 100%;
    height: 92px;
    background: var(--brand-blue);
    display: flex;
    align-items: center;
    justify-content: center;
    color: var(--text-light);
    font-size: 17px;
    font-weight: 400;
    white-space: nowrap;
  }
  .contact-band b { font-weight: 700; }
  .contact-band .sep { margin: 0 8px; }
</style>
</head>
<body>
  <main class="sheet">
    <section class="card card--front" aria-label="Card front">
      <div class="brand">
        <span class="brand__square"></span>
        <span class="brand__name">Quorvane</span>
      </div>
    </section>

    <section class="card card--back" aria-label="Card back">
      <div class="name-frame">
        <span class="name-frame__name">Martin Ellwood</span>
        <span class="name-frame__role">CEO</span>
      </div>
      <div class="contact-band">
        <span><b>P:</b> 0208 1234567</span><span class="sep">|</span>
        <span><b>M:</b> +44 7700123456</span><span class="sep">|</span>
        <span><b>E:</b> martin@quorvane.co.uk</span>
      </div>
    </section>
  </main>
</body>
</html>
```